Business Card Design

I need a business card design for a photography business that specializes in headshots and portraits.

Target Market(s)

Business professionals, actors, actresses

Industry/Entity Type

Business

Contact Information for Business Card

Cobalt Ridge Photography, Greg Whitlow, 5817 Kellerman Ave, Suite 416, Fort Wayne, IN 46915, 260.555.0187, www.cobaltridgephoto.example. greg.whitlow@cobaltridgephoto.example

Requirements
Must have
• The business card should state the type of photography services offered: headshots and portraits.

```html
<!DOCTYPE html>
<html lang="en">
<head>
<meta charset="utf-8">
<title>Cobalt Ridge Photography – Business Card</title>
<link href="https://fonts.googleapis.com/css2?family=Source+Sans+3:wght@400;600&display=swap" rel="stylesheet">
<style>
  :root {
    --page-bg: #ffffff;
    --card-bg: #070908;
    --name-grey: #dfe3e2;
    --text-grey: #d9dcdb;
    --accent-red: #8e0a06;
  }
  * { margin: 0; padding: 0; box-sizing: border-box; }
  html, body {
    width: 1200px;
    height: 1000px;
    overflow: hidden;
    background: var(--page-bg);
    font-family: "Source Sans 3", "Myriad Pro", Arial, sans-serif;
  }
  .card {
    position: absolute;
    left: 59px;
    top: 184px;
    width: 1082px;
    height: 631px;
    background: var(--card-bg);
  }
  .brand-mark {
    position: absolute;
    left: 486px;
    top: 92px;
    width: 110px;
    height: 110px;
  }
  .brand-name {
    position: absolute;
    left: 0;
    width: 100%;
    top: 270px;
    text-align: center;
    font-size: 70px;
    font-weight: 400;
    line-height: 1;
    color: var(--name-grey);
    letter-spacing: 0.2px;
  }
  .contact {
    position: absolute;
    left: 0;
    width: 100%;
    text-align: center;
    font-size: 22.5px;
    font-weight: 600;
    color: var(--text-grey);
    line-height: 1;
    white-space: nowrap;
  }
  .contact-primary { top: 437px; }
  .contact-online { top: 472px; }
  .divider { padding: 0 8px; }
  .services {
    position: absolute;
    left: 0;
    width: 1025px;
    top: 542px;
    text-align: center;
    font-size: 22.5px;
    font-weight: 600;
    color: var(--text-grey);
    line-height: 1;
  }
</style>
</head>
<body>
  <div class="card">
    <svg class="brand-mark" viewBox="0 0 110 110" aria-hidden="true">
      <circle cx="55" cy="55" r="48" fill="var(--accent-red)"/>
    </svg>
    <h1 class="brand-name">Cobalt Ridge Photography</h1>
    <p class="contact contact-primary">Greg Whitlow<span class="divider">|</span>5817 Kellerman Ave,&nbsp; Suite 416, Fort Wayne,&nbsp; IN 46915,260.555.0187</p>
    <p class="contact contact-online">www.cobaltridgephoto.example<span class="divider">|</span>greg.whitlow@cobaltridgephoto.example</p>
    <p class="services">Headshots and Portraits</p>
  </div>
</body>
</html>
```